New professional looking flyer for company

I need our flyer updated my flyer is the Lvb flyer Have attached current flyer so you know what services need to be listed. Want it to be in mainly dark colours like black and dark grey with pops of light grey, silver or white. i have added several photos for you to choose which ones work best with your design would like The photos to be in colour for the flyer. But can have a mix of greyscale if that works for your design j have attached another companies flyers as design ideas to show what I am looking for

Target Market(s)

new clients

Industry/Entity Type

transport and earthmoving

Colors

Designer to choose colors to be used in the design.

Requirements
Nice to have
• Look professional
Should not have
• No orange or red or green

```html
<!DOCTYPE html>
<html lang="en">
<head>
<meta charset="utf-8">
<title>Lvb Heavy Haulage Flyer</title>
<link href="https://fonts.googleapis.com/css2?family=Montserrat:ital,wght@0,400;0,600;0,700;0,800;1,400;1,800;1,900&display=swap" rel="stylesheet">
<style>
  :root{
    --stage:#e0e0e0;
    --ink:#121212;
    --dark:#1b1b1b;
    --charcoal:#2a2a2a;
    --silver:#c9c9c9;
    --silver-light:#ededed;
    --white:#ffffff;
    --text-grey:#555555;
    --line:#3a3a3a;
  }
  *{margin:0;padding:0;box-sizing:border-box}
  html,body{width:1200px;height:800px;overflow:hidden;background:var(--stage);font-family:"Montserrat",sans-serif}
  .flyer{position:absolute;left:342px;top:40px;width:516px;height:720px;background:var(--white);overflow:hidden}
  .hero-art{position:absolute;left:0;top:0}
  .tagline{position:absolute;left:38px;top:48px;color:var(--white);font-style:italic;font-weight:900;font-size:16.5px;line-height:16px;letter-spacing:.2px}
  .headline{position:absolute;left:30px;top:82px;font-style:italic;font-weight:900;font-size:38px;line-height:32px;letter-spacing:.5px;color:var(--silver-light)}
  .intro{position:absolute;left:29px;top:158px;width:270px;color:var(--white);font-style:italic;font-size:11.3px;line-height:15.2px}
  .brand{position:absolute;left:340px;top:62px;width:140px;text-align:center;color:var(--silver);font-weight:800;font-size:44px;line-height:44px;letter-spacing:2px}
  .brand small{display:block;font-size:12px;line-height:16px;letter-spacing:1px;font-weight:800}
  .services-title{position:absolute;left:24px;top:316px;font-style:italic;font-weight:800;font-size:21px;color:var(--ink)}
  .services-copy{position:absolute;left:27px;top:345px;width:214px;font-size:9.2px;line-height:15.2px;color:var(--text-grey);text-align:justify}
  .service-grid{position:absolute;left:25px;top:443px;width:461px;height:205px;border:1px solid var(--line);display:grid;grid-template-columns:166px 148px 1fr;grid-template-rows:58px 46px 50px 1fr;background:rgba(255,255,255,.9)}
  .service{display:flex;align-items:center;gap:10px;padding-left:10px;border-right:1px solid var(--line);border-bottom:1px solid var(--line);font-size:10px;line-height:14.5px;color:var(--charcoal)}
  .service:nth-child(3n){border-right:none}
  .service:nth-child(n+10){border-bottom:none}
  .service-mark{flex:0 0 25px;width:25px;height:25px;border-radius:50%;background:#ececec}
  .footer{position:absolute;left:0;top:657px;width:516px;height:63px;background:linear-gradient(180deg,#3a3a3a 0%,#1c1c1c 45%,#111 100%);color:var(--white)}
  .touch{position:absolute;left:25px;top:14px;line-height:18px}
  .touch .get{font-size:15px;letter-spacing:4px;font-weight:400}
  .touch .big{font-size:18px;font-weight:800;letter-spacing:.5px;border-bottom:1.5px solid var(--white);padding-bottom:1px}
  .contact{position:absolute;left:119px;display:flex;align-items:center;gap:7px;font-size:11.5px;font-weight:600}
  .contact.web{top:17px}
  .contact.mail{top:38px}
  .call{position:absolute;left:313px;top:17px;display:flex;gap:7px;align-items:center}
  .call-badge{width:25px;height:31px;background:var(--white);border-radius:3px;display:flex;align-items:center;justify-content:center}
  .call-text small{display:block;font-size:9.5px;font-weight:600;line-height:11px}
  .call-text strong{display:block;font-size:21px;font-weight:800;line-height:22px;letter-spacing:.5px}
</style>
</head>
<body>
<main class="flyer">
  <svg class="hero-art" width="516" height="450" viewBox="0 0 516 450">
    <defs>
      <linearGradient id="heroShade" x1="0" y1="0" x2="1" y2="1">
        <stop offset="0" stop-color="#2a2a2a"/>
        <stop offset=".55" stop-color="#1d1d1d"/>
        <stop offset="1" stop-color="#3a3a3a"/>
      </linearGradient>
      <linearGradient id="ring" x1="0" y1="0" x2="1" y2="1">
        <stop offset="0" stop-color="#f2f2f2"/>
        <stop offset=".5" stop-color="#8a8a8a"/>
        <stop offset="1" stop-color="#d8d8d8"/>
      </linearGradient>
      <linearGradient id="siteA" x1="0" y1="0" x2="0" y2="1">
        <stop offset="0" stop-color="#3f7fd6"/>
        <stop offset=".5" stop-color="#8aa6c2"/>
        <stop offset=".62" stop-color="#b86b3e"/>
        <stop offset="1" stop-color="#8a4a2a"/>
      </linearGradient>
      <linearGradient id="siteB" x1="0" y1="0" x2="0" y2="1">
        <stop offset="0" stop-color="#3b78cf"/>
        <stop offset=".45" stop-color="#6d8fb4"/>
        <stop offset=".6" stop-color="#7a4a30"/>
        <stop offset="1" stop-color="#c9c9cc"/>
      </linearGradient>
      <linearGradient id="siteC" x1="0" y1="0" x2="0" y2="1">
        <stop offset="0" stop-color="#4c86d8"/>
        <stop offset=".5" stop-color="#c9ccd3"/>
        <stop offset=".75" stop-color="#8a5436"/>
        <stop offset="1" stop-color="#6e3d24"/>
      </linearGradient>
    </defs>
    <polygon points="0,0 516,0 516,218 255,343 0,218" fill="#3a3a3a"/>
    <polygon points="0,0 516,0 516,210 255,334 0,210" fill="url(#heroShade)" role="img" aria-label="Photo of a road train truck at dusk on an outback road"/>
    <g role="img" aria-label="Photo of a loader filling a tipper truck on red dirt">
      <circle cx="320" cy="343" r="64" fill="url(#ring)"/>
      <circle cx="320" cy="343" r="57" fill="url(#siteB)"/>
    </g>
    <g role="img" aria-label="Photo of a water tanker road train on a work site">
      <circle cx="439" cy="343" r="64" fill="url(#ring)"/>
      <circle cx="439" cy="343" r="57" fill="url(#siteC)"/>
    </g>
    <g role="img" aria-label="Photo of an excavator and tipper truck beside a trench">
      <circle cx="381" cy="252" r="68" fill="url(#ring)"/>
      <circle cx="381" cy="252" r="61" fill="url(#siteA)"/>
    </g>
  </svg>

  <p class="tagline">FOR A SAFE,<br>RELIABLE HEAVY</p>
  <h1 class="headline">HAULAGE<br>SERVICE</h1>
  <p class="intro">We Offers a large range of services not listed so call us today for a personalised quote to suit your needs.</p>
  <div class="brand">LVB<small>Pty Ltd</small></div>

  <h2 class="services-title">Our Services</h2>
  <p class="services-copy">Lorem ipsum dolor sit amet, consectetur adipisicing elit, sed do eiusmod tempor incididunt ut labore et dolore magna aliqua. Lorem ipsum dolor sit amet, consectetur adipisicing elit, sed do eiusmod tempor incididunt ut</p>

  <section class="service-grid">
    <div class="service"><span class="service-mark"></span>Over size loads /<br>Hot Shot Loads</div>
    <div class="service"><span class="service-mark"></span>Sand &amp; Metal<br>Supply &amp; Cartage</div>
    <div class="service"><span class="service-mark"></span>Heavy Vehicle<br>Recovery Services</div>
    <div class="service"><span class="service-mark"></span>Road Train Tippers</div>
    <div class="service"><span class="service-mark"></span>Potable Water<br>Deliveries</div>
    <div class="service"><span class="service-mark"></span>Road Train<br>Flat Tops</div>
    <div class="service"><span class="service-mark"></span>Road Building /<br>Maintence</div>
    <div class="service"><span class="service-mark"></span>Drop Deck<br>Trailers</div>
    <div class="service"><span class="service-mark"></span>Earthworks</div>
    <div class="service"><span class="service-mark"></span>Mine Site accredited<br>equipment &amp; Operators</div>
    <div class="service"><span class="service-mark"></span>Road Train<br>Tankers</div>
    <div class="service"><span class="service-mark"></span>Traffic<br>Management</div>
  </section>

  <footer class="footer">
    <div class="touch"><div class="get">GET IN</div><span class="big">TOUCH</span></div>
    <div class="contact web">
      <svg width="16" height="16" viewBox="0 0 16 16" fill="none" stroke="#fff" stroke-width="1.3"><circle cx="8" cy="8" r="6.5"/><ellipse cx="8" cy="8" rx="3" ry="6.5"/><line x1="1.5" y1="8" x2="14.5" y2="8"/><line x1="2.5" y1="4.5" x2="13.5" y2="4.5"/><line x1="2.5" y1="11.5" x2="13.5" y2="11.5"/></svg>
      www.lvb.com.au
    </div>
    <div class="contact mail">
      <svg width="16" height="12" viewBox="0 0 16 12" fill="none" stroke="#fff" stroke-width="1.3"><rect x=".7" y=".7" width="14.6" height="10.6"/><polyline points=".7,.7 8,7 15.3,.7"/></svg>
      info@lvb.com.au
    </div>
    <div class="call">
      <div class="call-badge">
        <svg width="16" height="20" viewBox="0 0 16 20"><path d="M4 1 L7 1 L8 6 L5.5 7.5 Q6.5 11.5 9 13.5 L11 11.5 L15 13.5 L14.5 17 Q13 19 10 18.5 Q2 15 1.5 5 Q1.5 2 4 1 Z" fill="#1b1b1b"/></svg>
      </div>
      <div class="call-text"><small>More information call us</small><strong>1300 555 019</strong></div>
    </div>
  </footer>
</main>
</body>
</html>
```